Vortel Business card
Let's Build Future
Professional
Rakesh Milavan
Founder
Vortel Consulting & Software Solutions, Inc.
2817 Harlow Crest Road
Ashmere, IL 60418
rakeshm@postvela.com
please see the logo files to make it the same theme as the logo...
ai file
eps file
gif file
png logo
jpg
pdf file logo

```html
<!DOCTYPE html>
<html lang="en">
<head>
<meta charset="utf-8">
<title>Vortel Business Card</title>
<link href="https://fonts.googleapis.com/css2?family=Oswald:wght@400;600&family=Open+Sans:wght@400&display=swap" rel="stylesheet">
<style>
  :root {
    --page: #e8e5e0;
    --card-light: #ffffff;
    --card-dark: #4a4a4a;
    --brand-green: #a6c81a;
    --ink-soft: #8a8a8a;
  }
  * { margin: 0; padding: 0; box-sizing: border-box; }
  html, body {
    width: 1200px; height: 758px; overflow: hidden;
    background: var(--page);
  }
  .canvas { position: relative; width: 1200px; height: 758px; }
  .card {
    position: absolute; width: 524px; height: 284px;
    border-radius: 14px; overflow: hidden;
    box-shadow: 0 3px 10px rgba(0,0,0,0.18);
  }
  .card--front { left: 66px; top: 96px; background: var(--card-light); }
  .card--back-light { left: 632px; top: 96px; background: var(--card-light); }
  .card--back-dark { left: 338px; top: 430px; background: var(--card-dark); }

  .brand {
    position: absolute; left: 34px;
    display: flex; align-items: center; gap: 14px;
  }
  .brand__mark {
    width: 40px; height: 40px; background: var(--brand-green);
  }
  .brand__name {
    font-family: "Oswald", sans-serif; font-weight: 600;
    font-size: 58px; line-height: 1; letter-spacing: 2px;
    color: var(--brand-green);
  }
  .card--front .brand { top: 40px; }
  .card--back-light .brand,
  .card--back-dark .brand { top: 108px; left: 50%; transform: translateX(-50%); }

  .name-band {
    position: absolute; left: 0; top: 150px; width: 100%; height: 28px;
    background: var(--brand-green);
    font-family: "Oswald", sans-serif; font-size: 19px; line-height: 28px;
    color: #fff; padding-left: 120px;
  }
  .name-band__role { font-weight: 400; font-size: 15px; }
  .contact {
    position: absolute; left: 116px; top: 190px;
    font-family: "Open Sans", sans-serif; font-size: 12px; line-height: 18px;
    color: var(--ink-soft);
  }
  .contact__email { display: flex; align-items: center; gap: 6px; }
</style>
</head>
<body>
<div class="canvas">
  <section class="card card--front">
    <div class="brand">
      <div class="brand__mark"></div>
      <div class="brand__name">Vortel</div>
    </div>
    <div class="name-band">Rakesh Milavan <span class="name-band__role">| Founder</span></div>
    <div class="contact">
      <div>Vortel Consulting &amp; Software Solutions, Inc.</div>
      <div>2817 Harlow Crest Road</div>
      <div>Ashmere, IL 60418</div>
      <div class="contact__email">
        <svg width="10" height="10" viewBox="0 0 10 10" aria-hidden="true"><circle cx="5" cy="5" r="4" fill="none" stroke="#8a8a8a" stroke-width="1.4"/><circle cx="5" cy="5" r="1.6" fill="#8a8a8a"/></svg>
        rakeshm@postvela.com
      </div>
    </div>
  </section>

  <section class="card card--back-light">
    <div class="brand">
      <div class="brand__mark"></div>
      <div class="brand__name">Vortel</div>
    </div>
  </section>

  <section class="card card--back-dark">
    <div class="brand">
      <div class="brand__mark"></div>
      <div class="brand__name">Vortel</div>
    </div>
  </section>
</div>
</body>
</html>
```